The Lantern Harbor Summit (Poster or Color Flyer)

Unique and not too traditional design with Wording:
The Lantern Harbor Summit: The Deeper Message of God's Relentless Love
Friday Aug. 5 - Sunday the 7th
Denver 2016
www.TheLanternSummit.example
Updates
Project Deadline Extended
Reason: Our first experience with this type of design service was with 47Pixel, and we received 140 designs within a week.
We received only 2 designers submissions by our first 5 days with Mosaic Bench. We received an email that our time would be extended, which is much appreciated. The last 24 hours has brought in several new designs - which is great. However, we have a team of reviewers on our end - and due to Christmas break, will not be able to make a decision until January 4 or 5.
Can our deadline be moved to January 5? (at no charge?)
THANKS,
Trevor
Target Market(s)
General public. Professors. Pastors.
Requirements
Must have
- Basic info above.
Nice to have
- Subtle verses tucked into the graphics
- See www.TheQKTs.example for some of these,
- such as Romans 11:32, 1 John 2:2, 1 Timothy 4:10, John 12:32
Should not have
- Typical religious appearance.

```html
<!DOCTYPE html>
<html lang="en">
<head>
<meta charset="utf-8">
<title>The Lantern Harbor Summit – Poster</title>
<link rel="stylesheet" href="https://fonts.googleapis.com/css2?family=Cinzel:wght@400;500&family=Oswald:wght@300;400;500&family=Cormorant+SC:wght@500&display=swap">
<style>
  :root {
    --backdrop: #1c1c1d;
    --night-deep: #0a1c24;
    --night-teal: #12485a;
    --sky-blue: #2f7690;
    --stone-grey: #4f6e72;
    --stone-dark: #0f1e20;
    --ink-white: #f4f8fa;
    --ink-soft: #cfe2ea;
    --verse-ink: rgba(190, 220, 232, 0.42);
  }
  html, body {
    margin: 0;
    width: 1200px;
    height: 799px;
    overflow: hidden;
    background: var(--backdrop);
  }
  .poster {
    position: absolute;
    left: 306px;
    top: 20px;
    width: 588px;
    height: 760px;
    overflow: hidden;
    color: var(--ink-white);
  }
  .poster-photo {
    position: absolute;
    inset: 0;
    background:
      linear-gradient(225deg,
        var(--night-deep) 0%,
        var(--night-teal) 38%,
        var(--sky-blue) 55%,
        var(--stone-grey) 72%,
        var(--stone-dark) 100%);
  }
  .headline {
    position: absolute;
    right: 30px;
    top: 34px;
    margin: 0;
    text-align: right;
    font-family: "Cinzel", serif;
    font-weight: 400;
    line-height: 1;
    text-shadow: 0 0 8px rgba(255,255,255,0.35);
  }
  .headline-top { display: block; font-size: 62px; letter-spacing: 1px; }
  .headline-bottom { display: block; font-size: 43px; letter-spacing: 1px; margin-top: 4px; }
  .tagline {
    position: absolute;
    right: 30px;
    top: 160px;
    margin: 0;
    font-family: "Oswald", sans-serif;
    font-weight: 300;
    font-size: 18px;
    letter-spacing: 3.2px;
    text-transform: uppercase;
    color: var(--ink-soft);
  }
  .event-details {
    position: absolute;
    right: 30px;
    top: 206px;
    margin: 0;
    text-align: right;
    font-family: "Oswald", sans-serif;
    font-weight: 400;
    font-size: 19px;
    line-height: 1.55;
    color: var(--ink-white);
  }
  .event-details .site { font-weight: 500; font-size: 20px; margin-top: 8px; display: block; }
  .verse {
    position: absolute;
    margin: 0;
    font-family: "Cormorant SC", serif;
    font-weight: 500;
    font-size: 11px;
    letter-spacing: 1.4px;
    line-height: 1.5;
    color: var(--verse-ink);
    text-transform: uppercase;
  }
  .verse-top { right: 30px; top: 8px; width: 330px; text-align: right; }
  .verse-mid { left: 40px; top: 252px; width: 250px; }
  .verse-low { left: 290px; top: 460px; width: 270px; }
  .verse-base { left: 26px; top: 640px; width: 300px; }
</style>
</head>
<body>
  <main class="poster">
    <div class="poster-photo" role="img" aria-label="Photograph of an old stone fortress wall rising into a starry teal night sky with soft clouds"></div>

    <p class="verse verse-top">That is why we labor and strive, because we trust in the living God, who is the Savior of all people, especially of those who believe.</p>

    <h1 class="headline">
      <span class="headline-top">The Lantern</span>
      <span class="headline-bottom">Harbor Summit:</span>
    </h1>
    <p class="tagline">The Deeper Message of God's Relentless Love</p>

    <p class="event-details">
      Friday Aug. 5 - Sunday the 7th<br>
      Denver 2016
      <span class="site">www.TheLanternSummit.example</span>
    </p>

    <p class="verse verse-mid">For God has consigned all to disobedience, that He may have mercy on them all.</p>
    <p class="verse verse-low">He is the atoning sacrifice for our sins, and not only for ours but also for the sins of the whole world.</p>
    <p class="verse verse-base">And we have seen and testify that the Father has sent his Son to be the Savior of the world.</p>
  </main>
</body>
</html>
```